Bright-loop designs Business Card

embroidery printing

Target Market(s)

Businesses and public

Industry/Entity Type

Business

Contact Information for Business Card

Front of card..... Bright-loop designs .... Corin Maltby..... 868 512-7361.... Email... bright_loopdesigns@mailbrook.net

Back of card..... Bright-loop designs embroidery & artwork

Colors
000000

```html
<!DOCTYPE html>
<html lang="en">
<head>
<meta charset="utf-8">
<title>Bright-loop designs – Business Card</title>
<link rel="stylesheet" href="https://fonts.googleapis.com/css2?family=Arvo:ital,wght@0,400;0,700;1,400&display=swap">
<style>
  :root {
    --backdrop: #c9c9c9;
    --card-stock: #f1efe9;
    --card-edge: #7a2a1c;
    --ink: #1c1c1c;
    --accent-red: #e0393e;
  }
  html, body {
    margin: 0;
    padding: 0;
    width: 1200px;
    height: 849px;
    overflow: hidden;
    background: var(--backdrop);
  }
  .canvas {
    position: relative;
    width: 1200px;
    height: 849px;
    display: flex;
    align-items: center;
    justify-content: center;
    gap: 48px;
    font-family: "Arvo", Georgia, serif;
    color: var(--ink);
  }
  .card {
    position: relative;
    width: 500px;
    height: 286px;
    background: var(--card-stock);
    border-bottom: 4px solid var(--card-edge);
    box-sizing: border-box;
  }
  /* Logo side */
  .card--brand {
    display: flex;
    align-items: center;
    justify-content: center;
    gap: 16px;
  }
  .brand-dot {
    width: 26px;
    height: 26px;
    border-radius: 50%;
    background: var(--accent-red);
    flex: none;
  }
  .brand-name {
    font-weight: 700;
    font-size: 38px;
    letter-spacing: 0.5px;
    color: var(--ink);
    white-space: nowrap;
  }
  /* Contact side */
  .card--contact {
    padding: 70px 34px 0 34px;
  }
  .holder-name {
    margin: 0 0 34px 0;
    text-align: center;
    font-weight: 700;
    font-size: 30px;
    letter-spacing: 0.5px;
  }
  .contact-line {
    margin: 0 0 10px 0;
    font-size: 18px;
    white-space: nowrap;
  }
  .contact-line--phone {
    padding-left: 120px;
  }
  .contact-label {
    font-style: italic;
    font-size: 13px;
    margin-right: 8px;
  }
</style>
</head>
<body>
  <main class="canvas">
    <section class="card card--brand" aria-label="Card front">
      <span class="brand-dot"></span>
      <span class="brand-name">Bright-loop designs</span>
    </section>

    <section class="card card--contact" aria-label="Card back">
      <h1 class="holder-name">Corin Maltby</h1>
      <p class="contact-line contact-line--phone"><span class="contact-label">Phone.</span>868 512-7361</p>
      <p class="contact-line contact-line--email"><span class="contact-label">Email.</span>bright_loopdesigns@mailbrook.net</p>
    </section>
  </main>
</body>
</html>
```